Korvel Professional Services Website

Small website for company presence and information. Company is an IT/Telecom services company. We provide presales and installation services. Included are various company logos including color levels. Site doesn't have to use these exact colors in the logos, but should be complimentary if using different colors. It should have a professional business appearance.
Updates

My apologies for not being more responsive on the designs that have been submitted. I will be narrowing down the submissions and providing additional feedback next week. Thank you for your patience.

Project Deadline Extended
Reason: Sorry again for delays on picking designs. Work has me very busy and I've just not had the time to devote to this project. I am extending the design deadline for a few more days to give me time to make my final decisions. Thank you all for your patience. Stay tuned....

Target Market(s)

Telecom sales companies that sell Quenti telecom products.

Industry/Entity Type

Professional Service

Coding

Coded - Design and coding required

Number of Pages Required

5+ page

Font styles to use
Sans Serif

Colors
3276b5
0355a3
85abd2
85cae6
33a6d7
0692cd
ffffff

Requirements
Must have
• Professional design reflective of IT/Telecom business. A good reference website would be: http://www.lorbextech.example/. Looking for something similar in function and presence.
Nice to have
• Rolling photos highlighting our services. Traditional navigation across the top of all pages.
Should not have
• No motion video, flashy presentation or overly confused interface.

```html
<!DOCTYPE html>
<html lang="en">
<head>
<meta charset="utf-8">
<title>Korvel Professional Services</title>
<link href="https://fonts.googleapis.com/css2?family=Montserrat:wght@300;400;500;600;700&display=swap" rel="stylesheet">
<style>
:root{
  --orange:#e8864a;
  --navy:#1b2a52;
  --blue:#2f72b8;
  --blue-dark:#245f9e;
  --ink:#333a45;
  --muted:#8a8f98;
  --line:#e3e5e8;
  --grey-bg:#f4f4f4;
  --footer-dark:#23262b;
  --white:#ffffff;
}
*{box-sizing:border-box;margin:0;padding:0}
html,body{width:1200px;height:3309px;overflow:hidden}
body{font-family:"Montserrat",sans-serif;color:var(--ink);background:var(--white);position:relative}
.abs{position:absolute}
.section-title{position:absolute;left:0;width:1200px;text-align:center;font-size:25px;font-weight:400;color:var(--ink)}
.section-title strong{color:var(--navy);font-weight:700}
.section-sub{position:absolute;left:0;width:1200px;text-align:center;font-size:14px;color:var(--ink)}
.btn-outline{position:absolute;border:1.5px solid var(--orange);color:var(--orange);border-radius:20px;font-size:11px;text-align:center;line-height:30px;height:32px;width:112px}
.btn-solid{position:absolute;background:var(--orange);color:var(--white);border-radius:20px;font-size:11px;text-align:center;line-height:32px;height:32px;width:112px}

/* hero */
.hero{left:0;top:0;width:1200px;height:540px;background:linear-gradient(120deg,#c9d3dc 0%,#9aa4ae 35%,#7d8791 60%,#b3bcc4 100%)}
.hero-shade{left:0;top:0;width:1200px;height:540px;background:rgba(20,30,45,.25)}
.brand{left:155px;top:22px;display:flex;align-items:center;gap:10px;color:var(--white)}
.brand-mark{width:34px;height:34px;border-radius:50%;background:var(--white)}
.brand-name{font-size:28px;font-weight:700;letter-spacing:1px;line-height:1}
.brand-tag{font-size:8px;letter-spacing:1.5px;margin-top:3px}
.nav{left:435px;top:35px;display:flex;gap:20px;font-size:11px;font-weight:500;color:var(--white)}
.nav .active{border-bottom:2px solid var(--white);padding-bottom:6px}
.nav-home-icon{left:442px;top:12px;width:16px;height:16px;border-radius:50%;border:2px solid var(--white)}
.nav-contact{left:918px;top:26px;width:125px;height:34px;line-height:34px;border-radius:18px;background:var(--orange);color:var(--white);font-size:12px;text-align:center}
.hero-rule{left:0;top:86px;width:1200px;height:1px;background:rgba(255,255,255,.35)}
.hero-title{left:0;top:248px;width:1200px;text-align:center;color:var(--white);font-size:30px;font-weight:700}
.hero-sub{left:0;top:290px;width:1200px;text-align:center;color:var(--white);font-size:17px;font-weight:500}
.hero-btn{left:530px;top:336px;width:140px;height:36px;line-height:34px;border:1.5px solid var(--white);border-radius:20px;color:var(--white);font-size:12px;text-align:center}
.hero-arrow{top:247px;width:42px;height:42px;border-radius:50%}
.hero-arrow.prev{left:62px;border:2px solid var(--white)}
.hero-arrow.next{left:1093px;background:var(--orange)}
.hero-arrow svg{position:absolute;left:11px;top:11px}
.hero-arrow.prev svg{left:9px;top:9px}

/* services */
.service{position:absolute;top:684px;height:280px;border:1px solid var(--line);background:var(--white);text-align:center}
.service.featured{border:2px solid var(--orange)}
.service-icon{position:absolute;top:-18px;left:50%;margin-left:-36px;width:72px;height:78px}
.service h3{position:absolute;top:96px;left:0;width:100%;font-size:15px;font-weight:500;color:var(--navy);line-height:20px}
.service p{position:absolute;top:148px;left:14px;right:14px;font-size:10px;color:var(--muted);line-height:15px}
.service .btn-outline,.service .btn-solid{left:50%;margin-left:-56px;top:218px;width:112px}

/* about */
.about-band{left:0;top:1026px;width:613px;height:337px;background:var(--grey-bg)}
.about-logo{left:258px;top:1087px;display:flex;align-items:center;gap:10px}
.about-logo .brand-mark{background:var(--navy);width:32px;height:32px}
.about-logo .brand-name{color:var(--navy);font-size:26px}
.about-logo .brand-tag{color:var(--navy)}
.about-text{left:155px;top:1155px;width:385px;text-align:center;font-size:11px;color:var(--muted);line-height:17px}
.about-photo{left:613px;top:1026px;width:587px;height:337px;background:linear-gradient(135deg,#d9e2ea,#8f9aa6 55%,#5a6573)}

/* projects */
.project-tile{position:absolute}
.project-overlay{position:absolute;left:11px;top:11px;right:11px;bottom:11px;background:rgba(232,134,74,.9);color:var(--white);text-align:center}
.project-overlay span{position:absolute;top:42px;left:0;width:100%;font-size:14px;line-height:19px}

/* blog */
.blog-band{left:0;top:1963px;width:1200px;height:596px;background:var(--grey-bg)}
.blog-card{position:absolute;top:2107px;width:280px;height:390px;background:var(--white);border:1px solid var(--line)}
.blog-card.featured{box-shadow:0 4px 18px rgba(0,0,0,.12)}
.blog-img{position:absolute;left:23px;top:22px;width:234px;height:162px}
.blog-date{position:absolute;left:90px;top:170px;width:100px;height:24px;line-height:24px;border-radius:12px;background:var(--blue);color:var(--white);font-size:10px;text-align:center}
.blog-card h4{position:absolute;top:220px;left:20px;right:20px;text-align:center;font-size:12px;font-weight:600;color:var(--ink);line-height:17px}
.blog-card p{position:absolute;top:262px;left:30px;right:30px;text-align:center;font-size:11px;color:var(--muted);line-height:15px}
.blog-card .btn-outline,.blog-card .btn-solid{left:84px;top:334px}

/* partners */
.partner{position:absolute;top:2698px;width:136px;height:64px;border:1px solid var(--line);background:var(--white)}
.partner-badge{position:absolute;left:28px;top:24px;width:80px;height:16px;background:#d4d7dc;border-radius:2px}
.partner-arrows{left:977px;top:2636px;display:flex;align-items:center;gap:6px;color:var(--muted);font-size:14px}

/* footer */
.footer-left{left:0;top:2830px;width:588px;height:479px;background:linear-gradient(160deg,#3a7dc0,var(--blue-dark))}
.footer-right{left:588px;top:2830px;width:612px;height:479px;background:var(--footer-dark)}
.footer-title{left:267px;top:2905px;color:var(--white);font-size:22px;font-weight:600}
.contact-list{left:267px;top:2950px;color:var(--white);font-size:12px;line-height:19px}
.contact-list dt{font-weight:600}
.contact-list dd{margin-bottom:12px}
.socials{left:267px;top:3144px;display:flex;gap:8px}
.socials span{width:18px;height:18px;border-radius:50%;background:var(--white)}
.copyright{left:267px;top:3213px;color:var(--white);font-size:10px}
.field{position:absolute;left:664px;width:229px;border-bottom:1px solid rgba(255,255,255,.45);color:var(--white);font-size:11px;padding-bottom:14px}
.send{left:664px;top:3204px;width:125px;height:32px;line-height:32px;border-radius:18px;background:var(--orange);color:var(--white);font-size:12px;text-align:center}
.to-top{left:1084px;top:3205px;width:32px;height:32px;border-radius:50%;background:var(--orange)}
.to-top svg{position:absolute;left:10px;top:10px}
</style>
</head>
<body>

<!-- Hero -->
<div class="abs hero" role="img" aria-label="Business team meeting around a laptop in a bright office"></div>
<div class="abs hero-shade"></div>
<div class="abs brand">
  <span class="brand-mark"></span>
  <div><div class="brand-name">KORVEL</div><div class="brand-tag">PROFESSIONAL SERVICES</div></div>
</div>
<span class="abs nav-home-icon"></span>
<nav class="abs nav">
  <span class="active">HOME</span><span>ABOUT US</span><span>SERVICES</span><span>PORTFOLIO</span><span>BLOG</span><span>CONTACT US</span>
</nav>
<div class="abs nav-contact">Contact Us</div>
<div class="abs hero-rule"></div>
<div class="abs hero-arrow prev"><svg width="20" height="20" viewBox="0 0 20 20"><path d="M10 5 5 10l5 5M15 5l-5 5 5 5" fill="none" stroke="#fff" stroke-width="2"/></svg></div>
<div class="abs hero-arrow next"><svg width="20" height="20" viewBox="0 0 20 20"><path d="M5 5l5 5-5 5M10 5l5 5-5 5" fill="none" stroke="#fff" stroke-width="2"/></svg></div>
<h1 class="abs hero-title">Expertise. Insight. Experience.</h1>
<div class="abs hero-sub">The All New Korvel Now</div>
<div class="abs hero-btn">Explore More</div>

<!-- Services -->
<h2 class="section-title" style="top:598px">The Power of <strong>KORVEL</strong></h2>
<div class="section-sub" style="top:636px">We provide presales and installation services.</div>

<div class="service" style="left:157px;width:218px">
  <svg class="service-icon" viewBox="0 0 72 78"><path d="M36 2 68 20v38L36 76 4 58V20z" fill="#2f72b8"/><rect x="26" y="24" width="20" height="30" fill="none" stroke="#fff" stroke-width="2"/><path d="M26 34h20M26 44h20" stroke="#fff" stroke-width="2"/></svg>
  <h3>Data Center<br>Solutions</h3>
  <p>It's the brain, the place where the most critical systems are run. Data management...</p>
  <div class="btn-outline">Read More</div>
</div>
<div class="service featured" style="left:384px;width:203px">
  <svg class="service-icon" viewBox="0 0 72 78"><path d="M36 2 68 20v38L36 76 4 58V20z" fill="#e8864a"/><rect x="24" y="26" width="18" height="14" fill="none" stroke="#fff" stroke-width="2"/><rect x="38" y="36" width="10" height="16" fill="none" stroke="#fff" stroke-width="2"/><path d="M28 46h8" stroke="#fff" stroke-width="2"/></svg>
  <h3>Unified<br>Workspace</h3>
  <p>Communication, collaboration, and the "take your phone everywhere...</p>
  <div class="btn-solid">Read More</div>
</div>
<div class="service" style="left:613px;width:201px">
  <svg class="service-icon" viewBox="0 0 72 78"><path d="M36 2 68 20v38L36 76 4 58V20z" fill="#2f72b8"/><path d="M26 48h22a7 7 0 0 0 0-14 10 10 0 0 0-19-2 8 8 0 0 0-3 16z" fill="none" stroke="#fff" stroke-width="2"/></svg>
  <h3>Cloud<br>Services</h3>
  <p>What was business like before cloud? Energy consumption was rising, acquisition...</p>
  <div class="btn-outline">Read More</div>
</div>
<div class="service" style="left:840px;width:201px">
  <svg class="service-icon" viewBox="0 0 72 78"><path d="M36 2 68 20v38L36 76 4 58V20z" fill="#2f72b8"/><rect x="27" y="36" width="18" height="15" fill="none" stroke="#fff" stroke-width="2"/><path d="M30 36v-5a6 6 0 0 1 12 0v5" fill="none" stroke="#fff" stroke-width="2"/></svg>
  <h3>Security &amp; Risk<br>Management</h3>
  <p>Identity and access management, malware protection, compliance...</p>
  <div class="btn-outline">Read More</div>
</div>

<!-- About -->
<div class="abs about-band"></div>
<div class="abs about-logo">
  <span class="brand-mark"></span>
  <div><div class="brand-name">KORVEL</div><div class="brand-tag">PROFESSIONAL SERVICES</div></div>
</div>
<p class="abs about-text">There are many variations of passages of Lorem Ipsum available, but the majority have suffered alteration in some form, by injected humour, or randomised words which don't look even slightly believable. If you are going to use a passage of Lorem Ipsum, you need to be sure there isn't anything...</p>
<div class="btn-outline" style="left:289px;top:1267px;width:122px">Discover More</div>
<div class="abs about-photo" role="img" aria-label="Smiling colleagues in business attire discussing around a conference table"></div>

<!-- Projects -->
<h2 class="section-title" style="top:1420px">Our <strong>Project</strong></h2>
<div class="section-sub" style="top:1459px">Readable content of a page when looking.</div>
<div class="project-tile" style="left:157px;top:1502px;width:278px;height:400px;background:linear-gradient(160deg,#c9a347 0%,#6f7278 30%,#2e3137 65%,#cfd3d8 100%)" role="img" aria-label="Rows of server racks in a data center aisle"></div>
<div class="project-tile" style="left:459px;top:1502px;width:280px;height:124px;background:linear-gradient(135deg,#7b8796,#b9c1c9)" role="img" aria-label="Security and risk management project image">
  <div class="project-overlay"><span>Security &amp; Risk<br>Management</span>
    <svg style="position:absolute;left:122px;top:84px" width="14" height="14" viewBox="0 0 14 14"><path d="M6 8a3 3 0 0 0 4 0l2-2a3 3 0 0 0-4-4L7 3M8 6a3 3 0 0 0-4 0L2 8a3 3 0 0 0 4 4l1-1" fill="none" stroke="#fff" stroke-width="1.5"/></svg>
  </div>
</div>
<div class="project-tile" style="left:459px;top:1652px;width:280px;height:250px;background:linear-gradient(180deg,#b9d6ee 0%,#8fb4cf 45%,#5c8a6a 75%,#4d5359 100%)" role="img" aria-label="City skyline with a glowing connected network over a road"></div>
<div class="project-tile" style="left:763px;top:1502px;width:280px;height:400px;background:linear-gradient(150deg,#3f6b6d 0%,#2a2d33 40%,#6e5a4d 70%,#3a3d43 100%)" role="img" aria-label="Technician with a tablet working on network cabling"></div>

<!-- Blog -->
<div class="abs blog-band"></div>
<h2 class="section-title" style="top:2023px">Latest <strong>Blog</strong></h2>
<div class="section-sub" style="top:2060px">Learn the latest technology trends.</div>

<article class="blog-card" style="left:157px">
  <div class="blog-img" style="background:linear-gradient(135deg,#6f8fb8,#2d4f86 60%,#9ab1cc)" role="img" aria-label="Blue network cables plugged into a switch"></div>
  <div class="blog-date">Jun 20, 2016</div>
  <h4>There are many variations of passages of Lorem Ipsum</h4>
  <p>Evaluating the technical differences across the vendor landscape can be time lorem time...</p>
  <div class="btn-outline">Read More</div>
</article>
<article class="blog-card featured" style="left:459px">
  <div class="blog-img" style="background:linear-gradient(180deg,#cfe3f4,#7fa6cc 60%,#4b6d96)" role="img" aria-label="Team working at a table under a cloud computing graphic"></div>
  <div class="blog-date">Dec 03, 2016</div>
  <h4>There are many variations of passages of Lorem Ipsum</h4>
  <p>Evaluating the technical differences across the vendor landscape can be time lorem time...</p>
  <div class="btn-solid">Read More</div>
</article>
<article class="blog-card" style="left:763px">
  <div class="blog-img" style="background:linear-gradient(135deg,#eef2f6,#9cc3e4 55%,#d9a27c)" role="img" aria-label="Hands reviewing printed charts and graphs on a desk"></div>
  <div class="blog-date">May 31, 2016</div>
  <h4>There are many variations of passages of Lorem Ipsum</h4>
  <p>Evaluating the technical differences across the vendor landscape can be time lorem time...</p>
  <div class="btn-outline">Read More</div>
</article>

<!-- Partners -->
<h2 class="section-title" style="top:2618px">Our <strong>Partners</strong></h2>
<div class="section-sub" style="top:2654px">Key to Solution Excellence.</div>
<div class="abs partner-arrows">
  <svg width="22" height="10" viewBox="0 0 22 10"><path d="M22 5H3M7 1 3 5l4 4" fill="none" stroke="#2f72b8" stroke-width="2"/></svg>
  <span>/</span>
  <svg width="22" height="10" viewBox="0 0 22 10"><path d="M0 5h19M15 1l4 4-4 4" fill="none" stroke="#e8864a" stroke-width="2"/></svg>
</div>
<div class="partner" style="left:157px"><span class="partner-badge"></span></div>
<div class="partner" style="left:307px"><span class="partner-badge"></span></div>
<div class="partner" style="left:457px"><span class="partner-badge"></span></div>
<div class="partner" style="left:607px"><span class="partner-badge"></span></div>
<div class="partner" style="left:757px"><span class="partner-badge"></span></div>
<div class="partner" style="left:907px"><span class="partner-badge"></span></div>

<!-- Footer -->
<div class="abs footer-left"></div>
<div class="abs footer-right"></div>
<h3 class="abs footer-title">Get In Touch</h3>
<dl class="abs contact-list">
  <dt>Call Us:</dt><dd>+100-555-0142</dd>
  <dt>Email:</dt><dd>info@korvel.example</dd>
  <dt>Location:</dt><dd>58, Alder Lane, Westbrook,<br>CA-90210</dd>
</dl>
<div class="abs socials"><span></span><span></span><span></span><span></span></div>
<div class="abs copyright">© Copyright 2017 Korvel Professional Services</div>

<div class="field" style="top:2914px">Your Name</div>
<div class="field" style="top:2970px">Enter Email</div>
<div class="field" style="top:3028px">Subject</div>
<div class="field" style="top:3084px;padding-bottom:82px">Type Message</div>
<div class="abs send">➤ Send</div>
<div class="abs to-top"><svg width="12" height="12" viewBox="0 0 12 12"><path d="M2 8l4-4 4 4" fill="none" stroke="#fff" stroke-width="2"/></svg></div>

</body>
</html>
```